Verpackungsdesign für hochwertiges Haarparfum
Zielgruppe
Tovel's Method ist eine israelische Firma, die hochqualitative Haarprodukte und Haar Tools verkauft. Unsere Zielgruppe sind Frauen, die viel in Ihr Aussehen investieren und auf Ihr Äußeres sehr Wert legen.
Aufgabenstellung
Wir suchen nach einem Design für unsere zwei neuen Haarparfums. Es sollte teuer aussehen und das Design sollte modern und simpel sein. Die Flachen sind mit Milchglas und das Design wird auf die Flaschen gedruckt. Das Design muss komplett in Englischer Sprache sein.
Die Masse sind:
Höhe 7,7 cm
Umfang 11 cm
Es wird zwei Düfte geben.
1. The Nordic : Deckel wird Silber glänzend
2. The Celtic: Deckel wird Silber matt
Informationen die auf der Flasche sein sollten:
1. Firmen Logo (wird angehängt)
2. Name des Parfüms (The Nordic or the Celtic)
3. Longlasting Hair Fragrance
4. 30 ml
5. Includes essential hair vitamins and minerals
6. Alcohol and salt free

```html
<!DOCTYPE html>
<html lang="en">
<head>
<meta charset="utf-8">
<title>Tovel's Method – Nordic Hair Fragrance Label</title>
<link href="https://fonts.googleapis.com/css2?family=Cinzel:wght@400&family=Pinyon+Script&family=Source+Serif+4:wght@400&display=swap" rel="stylesheet">
<style>
  :root {
    --backdrop: #eeeeee;
    --label: #bcbcbc;
    --gold: #f5c30e;
    --ink: #ffffff;
  }
  * { margin: 0; padding: 0; box-sizing: border-box; }
  html, body {
    width: 1200px;
    height: 1096px;
    overflow: hidden;
    background: var(--backdrop);
  }
  .label {
    position: absolute;
    left: 336px;
    top: 48px;
    width: 528px;
    height: 1000px;
    background: var(--label);
    color: var(--ink);
    text-align: center;
  }
  .brand {
    position: absolute;
    top: 118px;
    left: 0;
    width: 100%;
    font-family: "Cinzel", serif;
    font-size: 15px;
    letter-spacing: 3px;
    line-height: 20px;
    color: var(--ink);
  }
  .scent-name {
    position: absolute;
    top: 292px;
    left: 0;
    width: 100%;
    font-family: "Cinzel", serif;
    font-size: 80px;
    line-height: 80px;
    color: var(--gold);
  }
  .scent-rule {
    position: absolute;
    top: 376px;
    left: 110px;
    width: 298px;
    height: 7px;
    border: 2px solid var(--ink);
  }
  .claim {
    position: absolute;
    top: 440px;
    left: 0;
    width: 100%;
    font-family: "Cinzel", serif;
    font-size: 24px;
    letter-spacing: 1px;
    color: var(--ink);
  }
  .wreath {
    position: absolute;
    top: 466px;
    left: 103px;
    width: 311px;
    height: 190px;
  }
  .product-type {
    position: absolute;
    top: 482px;
    left: 0;
    width: 100%;
    font-family: "Pinyon Script", cursive;
    font-size: 42px;
    line-height: 32px;
    color: var(--ink);
  }
  .product-type .line-one { display: block; padding-left: 40px; }
  .product-type .line-two { display: block; padding-right: 4px; }
  .benefits {
    position: absolute;
    top: 788px;
    left: 0;
    width: 100%;
    font-family: "Source Serif 4", serif;
    font-size: 16px;
    line-height: 20px;
    color: var(--ink);
  }
  .free-from {
    position: absolute;
    top: 853px;
    left: 0;
    width: 100%;
    font-family: "Source Serif 4", serif;
    font-size: 16px;
    color: var(--ink);
  }
  .volume {
    position: absolute;
    top: 916px;
    left: 0;
    width: 100%;
    font-family: "Cinzel", serif;
    font-size: 30px;
    color: var(--ink);
  }
  .volume .unit { font-size: 15px; letter-spacing: 1px; }
</style>
</head>
<body>
  <main class="label">
    <div class="brand">TOVEL'S<br>METHOD</div>

    <h1 class="scent-name">NORDIC</h1>
    <div class="scent-rule"></div>

    <p class="claim">LONGLASTING</p>

    <svg class="wreath" viewBox="0 0 311 190" role="img" aria-label="Gold laurel wreath ornament framing the product type">
      <path d="M10 10 C 0 110, 80 185, 155 188 C 230 185, 311 110, 300 10 C 290 60, 260 140, 155 160 C 50 140, 20 60, 10 10 Z" fill="var(--gold)"/>
    </svg>

    <p class="product-type">
      <span class="line-one">Hair</span>
      <span class="line-two">Fragrance</span>
    </p>

    <p class="benefits">Includes essential hair<br>vitamins and minerals</p>
    <p class="free-from">Alcohol and salt free</p>

    <p class="volume">30<span class="unit"> ML</span></p>
  </main>
</body>
</html>
```